Harborline Outpost Atlas needs a web design

We are launching a new website and need a web design. The website is going to list every military base and installment around the world with information on each base such as a description of the base, the history of the base, contact information at the base, address, lat/long of the base, and any other relevant information including images of the base. We need a home page with navigation menu and the design of the military base page so that every military base page is formatted the same for the referenced information. We have included an example of the content that may be found on the base page(s). We are also going to have the information available in spanish.

We also wanted to mention we will be building this website in wordpress.

We also wanted to note that in the format of each base page, we will have a frequently asked questions section with answers.

```html
<!DOCTYPE html>
<html lang="en">
<head>
<meta charset="utf-8">
<title>Harborline Outpost Atlas</title>
<link rel="stylesheet" href="https://fonts.googleapis.com/css2?family=Montserrat:wght@400;500;600;700&family=Lato:ital,wght@0,400;0,700;1,400&display=swap">
<style>
:root{
  --navy:#1f2348;
  --ink:#1c1c1c;
  --text:#3a3a3a;
  --muted:#555;
  --star:#f6b400;
  --soft:#f8f8f8;
  --footer:#000;
  --white:#fff;
}
*{box-sizing:border-box;margin:0;padding:0}
html,body{width:1200px;height:3033px;overflow:hidden;background:var(--white)}
body{font-family:'Lato',sans-serif;color:var(--text);position:relative}
a{color:inherit;text-decoration:none}

.site-header{position:absolute;top:0;left:0;width:1200px;height:100px}
.brand{position:absolute;left:97px;top:33px;font-family:'Montserrat',sans-serif;font-weight:500;font-size:23px;line-height:30px;color:var(--ink);white-space:nowrap}
.main-nav{position:absolute;left:444px;top:38px;display:flex;gap:48px;font-size:16px;color:#222;white-space:nowrap}
.lang{position:absolute;left:1066px;top:37px;font-size:18px;font-weight:700;color:#222;display:flex;align-items:center;gap:3px}

.hero{position:absolute;top:100px;left:0;width:1200px;height:562px;overflow:hidden}
.hero-photo{position:absolute;inset:0;background:
  radial-gradient(ellipse 340px 460px at 880px 330px,#1c2230 0%,#232834 55%,transparent 80%),
  linear-gradient(100deg,#5d5450 0%,#6e5f58 30%,#5a4c48 55%,#3b3532 75%,#6a5650 100%)}
.hero-shade{position:absolute;inset:0;background:linear-gradient(90deg,rgba(0,0,0,.25),rgba(0,0,0,0) 60%)}
.hero-kicker{position:absolute;left:100px;top:126px;font-family:'Montserrat',sans-serif;font-weight:600;font-size:39px;color:var(--white)}
.hero-title{position:absolute;left:96px;top:196px;font-family:'Montserrat',sans-serif;font-weight:700;font-size:50px;color:var(--white);white-space:nowrap}
.hero-search{position:absolute;left:100px;top:304px;width:485px;height:64px;border:2px solid var(--white);display:flex;align-items:center;padding:0 14px;color:var(--white);font-size:15px}
.hero-search svg{position:absolute;right:20px}
.hero-dots{position:absolute;top:512px;left:576px;display:flex;gap:7px}
.hero-dots span{width:12px;height:12px;border:2px solid var(--white);border-radius:50%}
.hero-dots span.on{background:var(--white)}

.featured-title{position:absolute;top:752px;width:1200px;text-align:center;font-family:'Montserrat',sans-serif;font-weight:500;font-size:36px;color:var(--ink)}
.base-card{position:absolute;left:150px;width:899px;height:242px;background:var(--white);box-shadow:0 0 12px rgba(0,0,0,.09);display:flex}
.base-photo{width:284px;height:242px;flex:none}
.base-body{position:relative;flex:1}
.base-name{position:absolute;left:31px;top:24px;font-family:'Montserrat',sans-serif;font-weight:500;font-size:24px;color:var(--ink);white-space:nowrap}
.stars{position:absolute;left:32px;top:68px;display:flex;gap:3px}
.base-desc{position:absolute;left:33px;top:104px;width:347px;font-size:15.5px;line-height:26.5px;text-align:justify;color:var(--text)}
.learn{position:absolute;left:33px;top:196px;font-family:'Montserrat',sans-serif;font-weight:700;font-size:15.5px;color:var(--navy);display:flex;align-items:center;gap:5px}
.base-contact{position:absolute;right:27px;top:82px;width:170px;text-align:right;font-size:14.5px;line-height:23px;color:var(--ink)}
.base-contact .phone{margin-bottom:16px}
.directions{position:absolute;right:27px;top:196px;font-family:'Montserrat',sans-serif;font-weight:700;font-size:15.5px;color:var(--navy)}

.view-all{position:absolute;left:519px;top:2021px;width:162px;height:52px;background:var(--navy);color:var(--white);font-family:'Montserrat',sans-serif;font-weight:700;font-size:15px;display:flex;align-items:center;justify-content:center}

.testimonials{position:absolute;top:2185px;left:0;width:1200px;height:494px;background:var(--soft)}
.quote-mark{position:absolute;font-family:'Montserrat',sans-serif;font-size:190px;line-height:1;color:#e6e6e6;font-weight:400}
.quote-open{left:164px;top:88px}
.quote-close{left:914px;top:255px}
.t-title{position:absolute;top:94px;width:1200px;text-align:center;font-family:'Montserrat',sans-serif;font-weight:700;font-size:31px;color:var(--ink)}
.t-rule{position:absolute;left:567px;top:137px;width:66px;height:3px;background:var(--navy)}
.t-text{position:absolute;left:238px;top:183px;width:724px;text-align:center;font-style:italic;font-size:16px;line-height:26.5px;color:var(--muted)}
.t-name{position:absolute;top:308px;width:1200px;text-align:center;font-family:'Montserrat',sans-serif;font-weight:600;font-size:16px;color:var(--ink)}
.t-stars{position:absolute;top:349px;left:566px;display:flex;gap:1px}
.t-dots{position:absolute;top:397px;left:555px;display:flex;gap:14px}
.t-dots span{width:21px;height:4px;background:#d6d6d6}
.t-dots span.on{background:var(--navy)}

.site-footer{position:absolute;top:2679px;left:0;width:1200px;height:354px;background:var(--footer);border-top:3px solid #4a4a4a;color:var(--white)}
.f-brand{position:absolute;left:97px;top:110px;font-family:'Montserrat',sans-serif;font-weight:500;font-size:23px;line-height:30px;white-space:nowrap}
.social{position:absolute;left:106px;top:214px;display:flex;gap:14px}
.social span{width:39px;height:39px;border:2px solid var(--white);border-radius:50%;display:block}
.f-col{position:absolute;top:80px}
.f-col h3{font-family:'Montserrat',sans-serif;font-weight:600;font-size:19px;margin-bottom:14px}
.f-col li{list-style:none;font-size:16px;line-height:25px;white-space:nowrap}
.col-links{left:443px}
.col-company{left:649px}
.col-contact{left:834px}
.col-contact li{display:flex;gap:12px;margin-bottom:9px;align-items:flex-start}
.col-contact svg{flex:none;margin-top:5px}
.copyright{position:absolute;top:296px;width:1200px;text-align:center;font-size:15px}
</style>
</head>
<body>

<header class="site-header">
  <div class="brand">Harborline Outpost Atlas</div>
  <nav class="main-nav">
    <a href="#">Home</a><a href="#">Military base directory</a><a href="#">Services</a><a href="#">Blog</a><a href="#">Contact Us</a>
  </nav>
  <div class="lang">EN <svg width="8" height="12" viewBox="0 0 8 12"><path d="M2 1l5 5-5 5" fill="none" stroke="#222" stroke-width="1.6"/></svg></div>
</header>

<section class="hero">
  <div class="hero-photo" role="img" aria-label="Uniformed soldier saluting in front of a flag"></div>
  <div class="hero-shade"></div>
  <div class="hero-kicker">Welcome to</div>
  <h1 class="hero-title">Harborline Outpost Atlas</h1>
  <div class="hero-search">Search by Military base
    <svg width="18" height="18" viewBox="0 0 18 18"><circle cx="7.5" cy="7.5" r="5.5" fill="none" stroke="#fff" stroke-width="2.4"/><path d="M11.5 11.5l5 5" stroke="#fff" stroke-width="2.6"/></svg>
  </div>
  <div class="hero-dots"><span></span><span class="on"></span><span></span></div>
</section>

<h2 class="featured-title">Featured Military base</h2>

<svg width="0" height="0" style="position:absolute">
  <defs>
    <symbol id="star" viewBox="0 0 20 20"><path d="M10 1l2.6 6 6.4.5-4.9 4.2 1.5 6.3L10 14.6 4.4 18l1.5-6.3L1 7.5l6.4-.5z" fill="#f6b400"/></symbol>
    <symbol id="go" viewBox="0 0 14 14"><circle cx="7" cy="7" r="7" fill="#1f2348"/><path d="M5.5 3.8L8.8 7l-3.3 3.2" fill="none" stroke="#fff" stroke-width="2"/></symbol>
  </defs>
</svg>

<article class="base-card" style="top:862px">
  <div class="base-photo" role="img" aria-label="Drone flying past mountains and hangars" style="background:linear-gradient(180deg,#b7c6d6 0%,#8e8a98 45%,#a08a73 70%,#7d6d5c 100%)"></div>
  <div class="base-body">
    <h3 class="base-name">Fort Calder Military Base:</h3>
    <div class="stars"><svg width="18" height="18"><use href="#star"/></svg><svg width="18" height="18"><use href="#star"/></svg><svg width="18" height="18"><use href="#star"/></svg><svg width="18" height="18"><use href="#star"/></svg><svg width="18" height="18"><use href="#star"/></svg></div>
    <p class="base-desc">Welcome to the official website page for Fort Calder, a historic and significant military base located in Westmere, USA.</p>
    <a class="learn" href="#">Learn More <svg width="14" height="14"><use href="#go"/></svg></a>
    <div class="base-contact"><div class="phone">(555) 014-3710</div>Fort Calder, WM, United States</div>
    <a class="directions" href="#">Directions</a>
  </div>
</article>

<article class="base-card" style="top:1152px">
  <div class="base-photo" role="img" aria-label="Aerial view of a five-sided headquarters building" style="background:linear-gradient(135deg,#4f5a3c 0%,#7a7a70 45%,#8d8b84 60%,#4d5638 100%)"></div>
  <div class="base-body">
    <h3 class="base-name">Lorem ipsum dolor sit amet :</h3>
    <div class="stars"><svg width="18" height="18"><use href="#star"/></svg><svg width="18" height="18"><use href="#star"/></svg><svg width="18" height="18"><use href="#star"/></svg><svg width="18" height="18"><use href="#star"/></svg><svg width="18" height="18"><use href="#star"/></svg></div>
    <p class="base-desc">Lorem ipsum dolor sit amet, consectetur adipiscing elit, sed do eiusmod tempor incididunt ut labore et dolore magna aliqua.</p>
    <a class="learn" href="#">Learn More <svg width="14" height="14"><use href="#go"/></svg></a>
    <div class="base-contact"><div class="phone">+1 (888) 888 8888</div>Lorem ipsum dolor sit amet</div>
    <a class="directions" href="#">Directions</a>
  </div>
</article>

<article class="base-card" style="top:1442px">
  <div class="base-photo" role="img" aria-label="Aerial view of base buildings among green fields" style="background:linear-gradient(170deg,#6f8a5a 0%,#6a6a62 40%,#5f7048 70%,#4f6a3a 100%)"></div>
  <div class="base-body">
    <h3 class="base-name">Lorem ipsum dolor sit amet :</h3>
    <div class="stars"><svg width="18" height="18"><use href="#star"/></svg><svg width="18" height="18"><use href="#star"/></svg><svg width="18" height="18"><use href="#star"/></svg><svg width="18" height="18"><use href="#star"/></svg><svg width="18" height="18"><use href="#star"/></svg></div>
    <p class="base-desc">Lorem ipsum dolor sit amet, consectetur adipiscing elit, sed do eiusmod tempor incididunt ut labore et dolore magna aliqua.</p>
    <a class="learn" href="#">Learn More <svg width="14" height="14"><use href="#go"/></svg></a>
    <div class="base-contact"><div class="phone">+1 (888) 888 8888</div>Lorem ipsum dolor sit amet</div>
    <a class="directions" href="#">Directions</a>
  </div>
</article>

<article class="base-card" style="top:1732px">
  <div class="base-photo" role="img" aria-label="Aircraft displayed on a grass airfield" style="background:linear-gradient(160deg,#8a8f86 0%,#6d8450 35%,#7b8a5a 65%,#5d7440 100%)"></div>
  <div class="base-body">
    <h3 class="base-name">Lorem ipsum dolor sit amet :</h3>
    <div class="stars"><svg width="18" height="18"><use href="#star"/></svg><svg width="18" height="18"><use href="#star"/></svg><svg width="18" height="18"><use href="#star"/></svg><svg width="18" height="18"><use href="#star"/></svg><svg width="18" height="18"><use href="#star"/></svg></div>
    <p class="base-desc">Lorem ipsum dolor sit amet, consectetur adipiscing elit, sed do eiusmod tempor incididunt ut labore et dolore magna aliqua.</p>
    <a class="learn" href="#">Learn More <svg width="14" height="14"><use href="#go"/></svg></a>
    <div class="base-contact"><div class="phone">+1 (888) 888 8888</div>Lorem ipsum dolor sit amet</div>
    <a class="directions" href="#">Directions</a>
  </div>
</article>

<a class="view-all" href="#">VIEW ALL</a>

<section class="testimonials">
  <div class="quote-mark quote-open">“</div>
  <div class="quote-mark quote-close">”</div>
  <h2 class="t-title">TESTIMONIALS</h2>
  <div class="t-rule"></div>
  <p class="t-text">Lorem ipsum dolor sit amet, consectetur adipiscing elit, sed do eiusmod tempor incididunt ut labore et dolore magna aliqua. Ut enim ad minim veniam, quis nostrud exercitation ullamco laboris nisi ut aliquip ex ea commodo consequat.Duis aute irure dolor in reprehenderit in voluptate velit esse cillum dolore eu fugiat nulla pariatur.</p>
  <div class="t-name">Lorem ipsum dolor</div>
  <div class="t-stars"><svg width="13" height="13"><use href="#star"/></svg><svg width="13" height="13"><use href="#star"/></svg><svg width="13" height="13"><use href="#star"/></svg><svg width="13" height="13"><use href="#star"/></svg><svg width="13" height="13"><use href="#star"/></svg></div>
  <div class="t-dots"><span></span><span class="on"></span><span></span></div>
</section>

<footer class="site-footer">
  <div class="f-brand">Harborline Outpost Atlas</div>
  <div class="social" aria-label="Social profiles"><span></span><span></span><span></span><span></span></div>
  <div class="f-col col-links">
    <h3>QUICK LINKS</h3>
    <ul><li>Home</li><li>Military base directory</li><li>Services</li><li>Blog</li><li>Contact Us</li></ul>
  </div>
  <div class="f-col col-company">
    <h3>COMPANY</h3>
    <ul><li>Terms &amp; Conditions</li><li>Privacy Policy</li><li>About Us</li><li>Support</li></ul>
  </div>
  <div class="f-col col-contact">
    <h3>CONTACT US</h3>
    <ul>
      <li><svg width="12" height="15" viewBox="0 0 12 15"><path d="M6 0a6 6 0 0 1 6 6c0 4-6 9-6 9S0 10 0 6a6 6 0 0 1 6-6z" fill="#fff"/><circle cx="6" cy="6" r="2.2" fill="#000"/></svg><span>Fort Calder, WM,<br>United States</span></li>
      <li><svg width="14" height="14" viewBox="0 0 14 14"><path d="M3 0l2.5 3.5-1.5 2c1 2 2.5 3.5 4.5 4.5l2-1.5L14 11l-1.5 2.5C6 14 0 8 .5 1.5z" fill="#fff"/></svg><span>(555) 014-3710</span></li>
      <li><svg width="14" height="11" viewBox="0 0 14 11"><rect width="14" height="11" rx="1" fill="#fff"/><path d="M0 1l7 5 7-5" fill="none" stroke="#000" stroke-width="1.4"/></svg><span>info@harborlineatlas.example</span></li>
    </ul>
  </div>
  <div class="copyright">©Copyrights 2023 Harborline Outpost Atlas &nbsp;| &nbsp; All Rights Reserved</div>
</footer>

</body>
</html>
```